Business card

would like a double sided business card made up with my logos provided.
Prefer card to have black background and to use the black logos, with matching blue writing for the text.
One side to just be the logo, (Try to use both the black logos)
the other side to have the logo and also my credentials/business information.

Covering all aspects of Carpentry and Building Services

Marcus Tolvey
Qualified Carpenter
Mob: 0417263948
Email: rkt.joinery@mailbright.com
ABN: 47 615 209 834

Industry/Entity Type

Business

Contact Information for Business Card

Marcus Tolvey
Qualified Carpenter
Mob: 0417263948
ABN: 47 615 209 834

Requirements
Must have
• Please try to use both the black logos and incorporate into the card.

```html
<!DOCTYPE html>
<html lang="en">
<head>
<meta charset="utf-8">
<title>RKT Joinery – Business Card</title>
<link href="https://fonts.googleapis.com/css2?family=Open+Sans:wght@400;600&family=Tinos:wght@400;700&display=swap" rel="stylesheet">
<style>
  :root {
    --page: #e9e9e7;
    --card-black: #0b0b0c;
    --card-blue: #3cb4e0;
    --blue-deep: #1f8fc0;
    --text-blue: #3fb6e6;
    --logo-grey: #5d5f63;
    --white: #ffffff;
    --rule: #8a8c90;
  }
  * { margin: 0; padding: 0; box-sizing: border-box; }
  html, body { width: 1200px; height: 1023px; overflow: hidden; }
  body {
    background: var(--page);
    font-family: "Open Sans", Arial, sans-serif;
    position: relative;
  }
  .card {
    position: absolute;
    left: 280px;
    width: 640px;
    height: 390px;
    background: var(--card-black);
    overflow: hidden;
    box-shadow: 0 6px 18px rgba(0,0,0,.18);
  }
  .card--brand { top: 70px; }
  .card--details { top: 563px; }
  .card-shape { position: absolute; inset: 0; width: 100%; height: 100%; }

  /* brand side */
  .brand-mark {
    position: absolute;
    left: 130px; top: 150px;
    display: flex; align-items: center; gap: 14px;
  }
  .brand-mark .dot { width: 26px; height: 26px; background: var(--card-blue); }
  .brand-mark .name {
    font-weight: 600; font-size: 50px; letter-spacing: 2px;
    color: var(--logo-grey);
  }
  .brand-rule {
    position: absolute; left: 50px; top: 270px;
    width: 380px; height: 2px; background: var(--rule);
  }
  .brand-tagline {
    position: absolute; left: 50px; top: 284px;
    color: var(--white); font-size: 17px;
  }

  /* details side */
  .holder { position: absolute; right: 40px; top: 30px; text-align: right; }
  .holder-name { color: var(--white); font-size: 24px; font-weight: 400; }
  .holder-rule { width: 120px; height: 3px; margin: 6px 0 6px auto; background: linear-gradient(90deg, transparent, var(--text-blue)); }
  .holder-role { color: var(--white); font-size: 13px; }
  .detail-mark {
    position: absolute; left: 30px; top: 196px;
    display: flex; align-items: center; gap: 10px;
  }
  .detail-mark .dot { width: 18px; height: 18px; background: var(--card-blue); }
  .detail-mark .name { color: var(--white); font-weight: 600; font-size: 30px; letter-spacing: 1px; }
  .contact {
    position: absolute; right: 40px; top: 124px;
    font-family: "Tinos", "Times New Roman", serif;
    font-weight: 700; font-size: 15px; line-height: 1.45;
    color: var(--text-blue); text-align: right;
  }
  .details-tagline {
    position: absolute; left: 30px; bottom: 30px;
    color: var(--white); font-size: 17px;
  }
</style>
</head>
<body>

<section class="card card--brand" aria-label="Business card, brand side">
  <svg class="card-shape" viewBox="0 0 640 390" preserveAspectRatio="none" aria-hidden="true">
    <defs>
      <linearGradient id="blueFace" x1="0" y1="0" x2="1" y2="1">
        <stop offset="0" stop-color="#52c4ec"/>
        <stop offset="1" stop-color="#2a9fd0"/>
      </linearGradient>
    </defs>
    <polygon points="470,0 640,0 640,390 470,390 560,280 560,110" fill="url(#blueFace)"/>
  </svg>
  <div class="brand-mark">
    <span class="dot"></span>
    <span class="name">RKT JOINERY</span>
  </div>
  <div class="brand-rule"></div>
  <p class="brand-tagline">Covering all aspects of Carpentry and Building Services</p>
</section>

<section class="card card--details" aria-label="Business card, details side">
  <svg class="card-shape" viewBox="0 0 640 390" preserveAspectRatio="none" aria-hidden="true">
    <defs>
      <linearGradient id="blueFlap" x1="0" y1="0" x2="1" y2="1">
        <stop offset="0" stop-color="#4fc2ea"/>
        <stop offset="1" stop-color="#2d9fd0"/>
      </linearGradient>
    </defs>
    <polygon points="0,252 380,312 640,228 640,390 0,390" fill="url(#blueFlap)"/>
  </svg>
  <div class="holder">
    <p class="holder-name">Marcus Tolvey</p>
    <div class="holder-rule"></div>
    <p class="holder-role">Qualified Carpenter</p>
  </div>
  <div class="detail-mark">
    <span class="dot"></span>
    <span class="name">RKT JOINERY</span>
  </div>
  <div class="contact">
    <p>Mob: 0417263948</p>
    <p>Email: rkt.joinery@mailbright.com</p>
    <p>ABN: 47 615 209 834</p>
  </div>
  <p class="details-tagline">Covering all aspects of Carpentry and Building Services</p>
</section>

</body>
</html>
```